Laundry Service Description Tri-Fold Brochure

My laundry business offers a service called "Velnora - Wet Cleaning"
I am after a design for a tri fold brochure to hand out to my customers. This will detail the benefits of wet cleaning vs dry cleaning.
I want the brochure to highlight the customer benefits NOT the business benefits.
I have attached the logo of our laundry which should be included
A couple of links here for more information and pdfs are attached:
https://brindlepartsupplyhub.com.au/laundry/velnora-wet-cleaning.html
https://www.quorv.co.za/wet-cleaning/
I have attached the design of our laundry window and ideally i want the brochure designed similar

```html
<!DOCTYPE html>
<html lang="en">
<head>
<meta charset="utf-8">
<title>Velnora Wet Cleaning – Tri-Fold Brochure</title>
<link rel="stylesheet" href="https://fonts.googleapis.com/css2?family=Montserrat:wght@300;400;600;800&display=swap">
<style>
  :root{
    --blue:#3b8ee0;
    --blue-light:#6aa9ea;
    --blue-pale:#cfe0f3;
    --black:#0f1013;
    --ink:#2a2c31;
    --grey-text:#5b5f66;
    --paper:#f6f7f8;
    --paper-cool:#e8ebef;
    --stage:#d7dade;
    --photo-dark:#3a4a60;
    --photo-mid:#7f97b6;
    --photo-light:#b9cbe0;
  }
  *{box-sizing:border-box;margin:0;padding:0}
  html,body{width:1200px;height:675px;overflow:hidden}
  body{background:var(--stage);font-family:"Montserrat",Arial,sans-serif;color:var(--ink);position:relative}
  .spread{position:absolute;top:134px;width:576px;height:406px;display:flex;box-shadow:0 6px 18px rgba(0,0,0,.18)}
  .spread--outside{left:16px}
  .spread--inside{left:608px}
  .panel{position:relative;width:192px;height:406px;background:var(--paper);overflow:hidden}
  .panel + .panel{border-left:1px solid rgba(0,0,0,.06)}
  .panel svg.shapes{position:absolute;inset:0;width:192px;height:406px}
  .panel .content{position:absolute;left:12px;right:12px}
  .heading{font-weight:400;color:var(--ink);font-size:11px;line-height:1.2}
  .heading--blue{color:var(--blue)}
  .divider{display:flex;gap:2px;margin:4px 0 6px;align-items:center}
  .divider span{display:block;height:1.5px;background:var(--blue)}
  .divider .bar{width:38px}
  .divider .dot{width:2px;height:2px;border-radius:50%}
  .body{font-size:5.6px;line-height:1.38;color:var(--grey-text)}
  .body p + p{margin-top:5px}
  .bullets{list-style:none;font-size:5.6px;line-height:1.38;color:var(--grey-text)}
  .bullets li{position:relative;padding-left:7px;margin-bottom:3px}
  .bullets li::before{content:"";position:absolute;left:0;top:2.4px;width:2.5px;height:2.5px;border-radius:50%;background:var(--ink)}
  .sub{color:var(--blue);font-size:7px;margin-bottom:4px}

  /* outside panel: benefits */
  .benefits .heading{color:var(--blue);font-size:10.5px}
  .eco{position:absolute;left:12px;right:12px;top:308px;color:#fff}
  .eco .heading{color:#fff;font-size:10px}
  .eco .body{color:#eef5fd}

  /* outside panel: contact */
  .contact{top:298px}
  .contact .title{font-weight:800;font-size:12px;letter-spacing:.5px;color:var(--black);margin-bottom:8px}
  .contact-list{list-style:none;font-size:6px;line-height:1.5;color:var(--ink)}
  .contact-list li{display:flex;gap:6px;align-items:flex-start;margin-bottom:2px}
  .contact-list svg{flex:none;width:7px;height:7px;margin-top:1px}

  /* cover */
  .brand{position:absolute;left:14px;right:10px;top:292px}
  .brand-name{display:flex;align-items:center;gap:6px;font-weight:600;font-size:19px;color:var(--blue);line-height:1}
  .brand-name i{display:block;width:9px;height:9px;border-radius:50%;background:var(--blue)}
  .brand-sub{font-weight:600;font-size:7.5px;letter-spacing:2px;color:var(--blue);margin-top:3px}
  .product{margin-top:10px;font-weight:800;font-size:15px;line-height:1.05;color:var(--ink)}
  .tagline{font-size:7px;color:var(--grey-text);margin-top:5px;padding-bottom:4px;border-bottom:1.5px solid var(--blue);display:inline-block}

  /* inside panels */
  .claim{top:208px;color:var(--blue-light);font-weight:300;font-size:14.5px;line-height:1.15}
  .intro{top:284px}
  .intro .heading{color:#fff;font-size:8px;margin-bottom:4px}
  .intro .body{color:#c9ccd2}
  .system{top:26px}
  .system .heading{font-size:11px}
  .unique{top:22px}
  .badge{position:absolute;left:56px;top:318px;width:80px;text-align:center;color:#fff;font-size:5.4px;font-weight:600;line-height:1.25}
  .badge .item{display:flex;flex-direction:column;align-items:center;margin-bottom:3px}
  .badge svg{width:6px;height:6px;margin-bottom:1px}
</style>
</head>
<body>

<!-- Outside of the brochure -->
<section class="spread spread--outside" aria-label="Brochure outside">

  <article class="panel benefits">
    <svg class="shapes" viewBox="0 0 192 406" aria-hidden="true">
      <polygon points="0,298 192,270 192,406 0,406" fill="var(--blue-light)"/>
      <polygon points="0,298 192,270 192,276 0,304" fill="var(--blue)"/>
    </svg>
    <div class="content" style="top:22px">
      <h2 class="heading">Simple and flexible</h2>
      <div class="divider"><span class="bar"></span><span class="dot"></span><span class="dot"></span><span class="dot"></span></div>
      <ul class="bullets">
        <li>Wet clean and wash regular laundry with the same machines</li>
        <li>Gentle on delicate fabrics like silk, wool and leather</li>
        <li>Clean a wide range of garments in one system</li>
        <li>Fast turnaround with no need for specialist solvents</li>
      </ul>
      <h2 class="heading" style="margin-top:14px">Natural and safe cleaning</h2>
      <div class="divider"><span class="bar"></span><span class="dot"></span><span class="dot"></span><span class="dot"></span></div>
      <ul class="bullets">
        <li>No air or water pollution – the process only uses water and biodegradable detergents</li>
        <li>Safe for sensitive skin and free of harsh chemical smells</li>
        <li>Garments come back fresh, soft and ready to wear</li>
      </ul>
    </div>
    <div class="eco">
      <h2 class="heading">Environmentally friendly</h2>
      <div class="divider"><span class="bar" style="background:#fff"></span></div>
      <p class="body">Wet cleaning uses water instead of toxic solvents, so it is kinder to our planet, our staff and you. Less energy, less waste and no hazardous residue left in your clothes.</p>
    </div>
  </article>

  <article class="panel" style="background:var(--paper-cool)">
    <svg class="shapes" viewBox="0 0 192 406">
      <defs>
        <linearGradient id="rackTone" x1="0" y1="0" x2="1" y2="1">
          <stop offset="0" stop-color="var(--photo-dark)"/>
          <stop offset="1" stop-color="var(--photo-mid)"/>
        </linearGradient>
        <linearGradient id="shirtsTone" x1="0" y1="0" x2="1" y2="1">
          <stop offset="0" stop-color="var(--photo-mid)"/>
          <stop offset="1" stop-color="var(--photo-dark)"/>
        </linearGradient>
      </defs>
      <rect x="0" y="0" width="192" height="210" fill="url(#rackTone)" role="img" aria-label="Photo: garments hanging on a clothes rack"/>
      <polygon points="130,0 192,0 192,60" fill="var(--black)"/>
      <polygon points="0,150 192,96 192,104 0,158" fill="var(--black)" opacity=".85"/>
      <polygon points="0,166 192,112 192,120 0,174" fill="var(--black)" opacity=".85"/>
      <polygon points="0,182 192,128 192,136 0,190" fill="var(--black)" opacity=".85"/>
      <polygon points="0,210 192,150 192,205 0,262" fill="var(--black)"/>
      <polygon points="0,262 192,205 192,406 0,406" fill="var(--paper-cool)"/>
      <polygon points="90,178 142,208 142,262 90,292 38,262 38,208" fill="var(--blue)"/>
      <polygon points="90,186 135,212 135,258 90,284 45,258 45,212" fill="url(#shirtsTone)" role="img" aria-label="Photo: shirts on hangers"/>
    </svg>
    <div class="content contact">
      <h2 class="title">CONTACT US</h2>
      <ul class="contact-list">
        <li><svg viewBox="0 0 10 10" aria-hidden="true"><path d="M2 1l2 2-1 1.3a6 6 0 0 0 2.7 2.7L7 6l2 2-1.3 1.5C4.6 9.3.7 5.4.5 2.3z" fill="var(--ink)"/></svg>000 123 456 789</li>
        <li><svg viewBox="0 0 10 10" aria-hidden="true"><circle cx="5" cy="5" r="4.2" fill="none" stroke="var(--ink)" stroke-width="1"/><path d="M1 5h8M5 1c-2 2.5-2 5.5 0 8M5 1c2 2.5 2 5.5 0 8" fill="none" stroke="var(--ink)" stroke-width=".8"/></svg>www.websiteurl.com</li>
        <li><svg viewBox="0 0 10 10" aria-hidden="true"><rect x=".8" y="2" width="8.4" height="6" fill="none" stroke="var(--ink)" stroke-width="1"/><path d="M1 2.3l4 3 4-3" fill="none" stroke="var(--ink)" stroke-width="1"/></svg>company@domain.com</li>
        <li><svg viewBox="0 0 10 10" aria-hidden="true"><path d="M5 9.5S1.8 5.8 1.8 3.7a3.2 3.2 0 0 1 6.4 0C8.2 5.8 5 9.5 5 9.5z" fill="var(--ink)"/><circle cx="5" cy="3.7" r="1.1" fill="var(--paper-cool)"/></svg>Your Address, Office Location,<br>Street Name, Country 4545</li>
      </ul>
    </div>
  </article>

  <article class="panel">
    <svg class="shapes" viewBox="0 0 192 406">
      <defs>
        <linearGradient id="suitTone" x1="0" y1="0" x2="1" y2="1">
          <stop offset="0" stop-color="var(--photo-light)"/>
          <stop offset=".55" stop-color="var(--photo-dark)"/>
          <stop offset="1" stop-color="#1d2330"/>
        </linearGradient>
      </defs>
      <rect x="0" y="0" width="192" height="100" fill="var(--black)"/>
      <polygon points="0,100 60,62 192,34 192,96 0,130" fill="var(--blue)"/>
      <polygon points="0,130 192,96 192,406 0,406" fill="var(--paper)"/>
      <polygon points="18,118 192,78 192,236 108,282 18,240" fill="url(#suitTone)" role="img" aria-label="Photo: dark suit jacket in front of a rail of shirts"/>
      <rect x="0" y="396" width="192" height="10" fill="var(--blue)"/>
    </svg>
    <div class="brand">
      <div class="brand-name">Calderwick <i></i></div>
      <div class="brand-sub">Laundry Services</div>
      <h1 class="product">Velnora<br>Wet Cleaning</h1>
      <p class="tagline">Velnora Incredibly efficient</p>
    </div>
  </article>
</section>

<!-- Inside of the brochure -->
<section class="spread spread--inside" aria-label="Brochure inside">

  <article class="panel">
    <svg class="shapes" viewBox="0 0 192 406">
      <defs>
        <linearGradient id="hangerTone" x1="0" y1="0" x2="1" y2="1">
          <stop offset="0" stop-color="#e9e3dc"/>
          <stop offset=".6" stop-color="var(--photo-light)"/>
          <stop offset="1" stop-color="var(--photo-mid)"/>
        </linearGradient>
      </defs>
      <polygon points="0,0 192,0 192,140 0,162" fill="url(#hangerTone)" role="img" aria-label="Photo: hand holding a shirt on a hanger in a garment bag"/>
      <polygon points="0,162 192,140 192,170 0,196" fill="var(--blue)"/>
      <polygon points="0,196 192,170 192,406 0,406" fill="var(--black)"/>
      <polygon points="120,190 192,180 192,250" fill="var(--blue)" opacity=".9"/>
    </svg>
    <p class="content claim">Velnora<br>cleans 100%<br>of garments,<br>100% of the time.</p>
    <div class="content intro">
      <h2 class="heading">What is Velnora?</h2>
      <p class="body">Velnora is a new alternative to dry cleaning that is now available. Velnora by Harlowe is a dry-to-dry wet cleaning process that has been developed and tested in Europe over the past 10 years. It is an environmentally friendly, water based garment care system that has gone through extensive testing with all fabric types to ensure it is state of the art and a level above traditional wet cleaning.</p>
    </div>
  </article>

  <article class="panel">
    <svg class="shapes" viewBox="0 0 192 406">
      <defs>
        <linearGradient id="towelTone" x1="0" y1="0" x2="0" y2="1">
          <stop offset="0" stop-color="var(--photo-light)"/>
          <stop offset="1" stop-color="#8aa4c0"/>
        </linearGradient>
      </defs>
      <polygon points="0,250 192,198 192,226 0,278" fill="var(--blue)"/>
      <polygon points="0,278 192,226 192,236 0,406" fill="var(--black)"/>
      <polygon points="60,268 192,232 192,406 28,406 20,330" fill="url(#towelTone)" role="img" aria-label="Photo: stack of folded towels"/>
    </svg>
    <div class="content system">
      <h2 class="heading">What makes up a<br>Velnora system?</h2>
      <div class="divider"><span class="bar"></span><span class="dot"></span><span class="dot"></span><span class="dot"></span></div>
      <p class="sub">There are 4 elements:</p>
      <ul class="bullets">
        <li>a Harlowe washer and dryer</li>
        <li>factory developed Velnora programming for the washer and dryer</li>
        <li>Velnora detergents including specialised spotting agents for all stain types and a detergent feed system</li>
        <li>finishing or ironing equipment (the system can be used with existing finishing and ironing equipment to save you money)</li>
      </ul>
      <p class="body" style="margin-top:5px">We can supply all washing, drying, ironing and finishing equipment to complete the process. Enquire with us today.</p>
    </div>
  </article>

  <article class="panel">
    <svg class="shapes" viewBox="0 0 192 406">
      <polygon points="0,318 192,300 192,406 0,406" fill="var(--black)"/>
      <polygon points="130,306 192,300 192,406 150,406" fill="var(--blue)"/>
      <polygon points="96,306 138,330 138,380 96,404 54,380 54,330" fill="var(--blue)" stroke="#fff" stroke-width="2"/>
    </svg>
    <div class="content unique">
      <h2 class="heading">Why is Velnora so unique?</h2>
      <div class="divider"><span class="bar"></span><span class="dot"></span><span class="dot"></span><span class="dot"></span></div>
      <div class="body">
        <p>Velnora is proven to clean 100% of garments, 100% of the time. This includes silk garments which keep their shape and colour beautifully when cleaned using a Velnora system, leather jackets, household textiles, furniture coverings and fire-proof garments.</p>
        <p>Oil and grease stains are also no problem for a Velnora system which offers superior stain removal, even on the most delicate of fabrics. The Velnora spotting chemicals help remove all types of stains, without the use of toxic chemicals. There is no need to hang garments (saving you space) and no additional time involved in carrying out the process when compared with dry cleaning.</p>
        <p>There's a lot to be excited about with Velnora, and the fact that it is environmentally friendly is just one of these aspects. The Velnora process only uses water (and uses this sparingly) and biodegradable detergents. Not only is this better for our environment, but better for the health of staff using the system. Garments smell fresh and clean, with no toxic fumes.</p>
        <p>What's more, it's completely versatile. A Harlowe Velnora system can be used for dry cleanable garments as well as commercial laundry. Simply set the machines program to clean a load of woollens, silks or the most delicate of wedding dresses and on the next load select the program for regular laundry such as sheets and towels. It's that simple.</p>
      </div>
    </div>
    <div class="badge">
      <div class="item"><svg viewBox="0 0 10 10" aria-hidden="true"><circle cx="5" cy="5" r="4.5" fill="#fff"/><path d="M2.8 5.2l1.5 1.5 3-3.2" fill="none" stroke="var(--blue)" stroke-width="1.2"/></svg>Advanced<br>Wet Cleaning</div>
      <div class="item"><svg viewBox="0 0 10 10" aria-hidden="true"><circle cx="5" cy="5" r="4.5" fill="#fff"/><path d="M2.8 5.2l1.5 1.5 3-3.2" fill="none" stroke="var(--blue)" stroke-width="1.2"/></svg>Unrivalled Results</div>
      <div class="item"><svg viewBox="0 0 10 10" aria-hidden="true"><circle cx="5" cy="5" r="4.5" fill="#fff"/><path d="M2.8 5.2l1.5 1.5 3-3.2" fill="none" stroke="var(--blue)" stroke-width="1.2"/></svg>Eco Alternative</div>
    </div>
  </article>
</section>

</body>
</html>
```